Business cards for property management company

Need new business cards designed for our property management company and rental community, Amber Knoll Commons. These cards will be primarily picked up by rental applicants.

May be single or double sided design.

I need cards for two different people, listed below. The design can be the same for both, and the only information that will be different is name and email address.

Industry/Entity Type

Property Management

Requirements
Must have
• US standard business card - 2''x3.5'' horizontal design.

1. Logo (attached). The text does not have to stay below the logo, but the card does need to say "Amber Knoll Commons" somewhere on it (does not have to be same font as logo, but those fonts are Americana Extra Bold and BlackJack if needed).
2. Name: one with "Lena Halvorsen" and one with "Dorian Halvorsen"
3. Email address: one with "lena@amberknollhub.com" and one with "dorian@amberknollhub.com"
4. Web address: amberknollhub.com
5. Phone: 281.555.0182
6. Address: 7390 Whitlock Avenue, Dickinson, Texas 77512 (zip code may me omitted, at your discretion)
Should not have
• No rounded corners or special cuts.

No bevel, emboss or shadow effects.

As a note, please do not use our website as a basis for color or design schemes. We are working on a redesign, based around the new logo (attached to brief).

```html
<!DOCTYPE html>
<html lang="en">
<head>
<meta charset="UTF-8">
<title>Amber Knoll Commons — Business Cards</title>
<link rel="stylesheet" href="https://fonts.googleapis.com/css2?family=Roboto+Condensed:wght@300;400&family=Roboto+Serif:wght@400&display=swap">
<style>
  :root {
    --page-bg: #ffffff;
    --card-bg: #07080a;
    --brand-green: #3f9a3a;
    --label-blue: #1ba2c9;
    --card-w: 583px;
    --card-h: 335px;
  }
  html, body {
    margin: 0;
    padding: 0;
    width: 1053px;
    height: 1200px;
    overflow: hidden;
    background: var(--page-bg);
  }
  .sheet {
    position: relative;
    width: 1053px;
    height: 1200px;
  }
  .business-card {
    position: absolute;
    width: var(--card-w);
    height: var(--card-h);
    background: var(--card-bg);
    overflow: hidden;
  }
  .business-card--lena { left: 280px; top: 215px; }
  .business-card--dorian { left: 291px; top: 642px; }

  .brand-mark {
    position: absolute;
    left: 30px;
    top: 95px;
    width: 170px;
    margin: 0;
    font-family: "Roboto Condensed", "Arial Narrow", sans-serif;
    font-weight: 400;
    font-size: 32px;
    line-height: 1.08;
    color: var(--brand-green);
  }

  .holder-name {
    position: absolute;
    left: 230px;
    top: 78px;
    margin: 0;
    font-family: "Roboto Condensed", "Arial Narrow", sans-serif;
    font-weight: 300;
    font-size: 42px;
    letter-spacing: 0.5px;
    color: var(--brand-green);
    white-space: nowrap;
  }
  .business-card--dorian .holder-name { left: 240px; top: 70px; }

  .contact-list {
    position: absolute;
    left: 345px;
    top: 224px;
    margin: 0;
    font-family: "Roboto Serif", "Times New Roman", serif;
    font-weight: 400;
    font-size: 13px;
    transform: scaleX(0.66);
    transform-origin: left top;
  }
  .contact-row {
    display: flex;
    height: 26px;
    align-items: center;
    white-space: nowrap;
  }
  .contact-row dt {
    width: 98px;
    color: var(--label-blue);
  }
  .contact-row dd {
    margin: 0;
    color: var(--brand-green);
  }
  .contact-row dd::before { content: ": "; }
  .contact-row--web { font-size: 14px; }
  .contact-row--web dt { width: auto; padding-right: 5px; }
  .contact-row--address { font-size: 10.5px; }
</style>
</head>
<body>
<main class="sheet">

  <article class="business-card business-card--lena">
    <p class="brand-mark">Amber<br>Knoll<br>Commons</p>
    <h1 class="holder-name">Lena Halvorsen</h1>
    <dl class="contact-list">
      <div class="contact-row"><dt>Phone</dt><dd>281.555.0182</dd></div>
      <div class="contact-row"><dt>email</dt><dd>lena@amberknollhub.com</dd></div>
      <div class="contact-row contact-row--web"><dt>Web address</dt><dd>amberknollhub.com</dd></div>
      <div class="contact-row contact-row--address"><dt>Address</dt><dd>7390 Whitlock Avenue, Dickinson, Texas 77512</dd></div>
    </dl>
  </article>

  <article class="business-card business-card--dorian">
    <p class="brand-mark">Amber<br>Knoll<br>Commons</p>
    <h1 class="holder-name">Dorian Halvorsen</h1>
    <dl class="contact-list">
      <div class="contact-row"><dt>Phone</dt><dd>281.555.0182</dd></div>
      <div class="contact-row"><dt>email</dt><dd>dorian@amberknollhub.com</dd></div>
      <div class="contact-row contact-row--web"><dt>Web address</dt><dd>amberknollhub.com</dd></div>
      <div class="contact-row contact-row--address"><dt>Address</dt><dd>7390 Whitlock Avenue, Dickinson, Texas 77512</dd></div>
    </dl>
  </article>

</main>
</body>
</html>
```